Cosmetic injections clinic needs a fresh looking business card

We need a business card using the supplied logo and color scheme to attract future clients to our clinic. It should be modern and fresh, eye catching and not too busy. Simple and to the point is best. I would like two sided designs with the front indicating address and contact information, and the back in full color with white logo and descriptive information also provided.
Target Market(s)
Clients looking for non surgical beauty enhancements.
Contact Information for Business Card
MeloraSkin
14, 618 Birchmont Way
Larkfield, Westmere
K2P 7W3
Phone: 587-412-6630
Email: info@meloraskin.com
Requirements
Must have
- -Logo supplied with the name and address of the clinic
- -Back of card in full color with white logo with A small line of text indicating both of the following: Anti aging consultants and cosmetic injectables
- Located inside the Voyager Wellness Group

```html
<!DOCTYPE html>
<html lang="en">
<head>
<meta charset="utf-8">
<title>MeloraSkin Business Card</title>
<link href="https://fonts.googleapis.com/css2?family=Montserrat:wght@500;600&family=Roboto:wght@400;500&family=Great+Vibes&display=swap" rel="stylesheet">
<style>
  :root {
    --brand-purple: #5b3a96;
    --brand-violet: #6d4aa8;
    --brand-pink: #e0449a;
    --ink: #1f1f24;
    --paper: #ffffff;
    --backdrop: #e4e4e6;
  }
  * { margin: 0; padding: 0; box-sizing: border-box; }
  html, body { width: 1200px; height: 1200px; overflow: hidden; }
  body {
    background: var(--backdrop);
    display: flex;
    flex-direction: column;
    align-items: center;
    justify-content: center;
    gap: 60px;
  }
  .card {
    position: relative;
    width: 880px;
    height: 503px;
    border-radius: 40px;
    overflow: hidden;
    box-shadow: 0 10px 30px rgba(0,0,0,0.12);
  }
  /* Back side */
  .card--back {
    background: var(--brand-purple);
    display: flex;
    flex-direction: column;
    align-items: center;
    justify-content: center;
    color: var(--paper);
  }
  .wordmark {
    display: flex;
    align-items: center;
    gap: 18px;
    font-family: "Montserrat", sans-serif;
    font-weight: 600;
    font-size: 64px;
    letter-spacing: 1px;
    white-space: nowrap;
  }
  .wordmark__dot {
    width: 70px;
    height: 70px;
    border-radius: 50%;
    background: currentColor;
  }
  .card--back .wordmark { color: var(--paper); }
  .tagline {
    margin-top: 22px;
    font-family: "Great Vibes", cursive;
    font-size: 36px;
    color: var(--paper);
  }
  /* Front side */
  .card--front { background: var(--paper); }
  .card__wave {
    position: absolute;
    inset: 0;
    width: 100%;
    height: 100%;
  }
  .brand-block {
    position: absolute;
    left: 70px;
    top: 200px;
  }
  .card--front .wordmark { color: var(--brand-violet); font-size: 52px; }
  .card--front .wordmark__dot { width: 58px; height: 58px; }
  .location-note {
    margin-top: 18px;
    font-family: "Montserrat", sans-serif;
    font-weight: 500;
    font-size: 19px;
    color: var(--ink);
    white-space: nowrap;
  }
  .contact-list {
    position: absolute;
    left: 560px;
    top: 70px;
    list-style: none;
    font-family: "Roboto", sans-serif;
    font-weight: 500;
    font-size: 21px;
    line-height: 1.2;
    color: var(--ink);
  }
  .contact-list li {
    display: flex;
    align-items: flex-start;
    gap: 16px;
    margin-bottom: 20px;
    white-space: nowrap;
  }
  .contact-list svg { flex: none; width: 24px; height: 24px; margin-top: 1px; }
  .contact-list .icon { fill: var(--brand-pink); }
</style>
</head>
<body>

  <section class="card card--back" aria-label="Card back">
    <div class="wordmark"><span class="wordmark__dot"></span>MeloraSkin</div>
    <p class="tagline">Anti aging consultants &amp; cosmetic injectables</p>
  </section>

  <section class="card card--front" aria-label="Card front">
    <svg class="card__wave" viewBox="0 0 880 503" preserveAspectRatio="none" aria-hidden="true">
      <path d="M0 445 C 220 380, 420 360, 600 340 S 820 290, 880 250" fill="none" stroke="var(--brand-violet)" stroke-width="7"/>
    </svg>

    <div class="brand-block">
      <div class="wordmark"><span class="wordmark__dot"></span>MeloraSkin</div>
      <p class="location-note">Located inside the Voyager Wellness Group</p>
    </div>

    <ul class="contact-list">
      <li>
        <svg viewBox="0 0 24 24" aria-hidden="true"><path class="icon" d="M12 1a7 7 0 0 0-7 7c0 5 7 12 7 12s7-7 7-12a7 7 0 0 0-7-7zm0 9.5A2.5 2.5 0 1 1 12 5.5a2.5 2.5 0 0 1 0 5z"/><rect class="icon" x="5" y="21.5" width="14" height="2" rx="1"/></svg>
        <span>14, 618 Birchmont Way<br>Larkfield, Westmere<br>K2P 7W3</span>
      </li>
      <li>
        <svg viewBox="0 0 24 24" aria-hidden="true"><path class="icon" d="M6.6 10.8a15.1 15.1 0 0 0 6.6 6.6l2.2-2.2a1 1 0 0 1 1-.25 11.4 11.4 0 0 0 3.6.57 1 1 0 0 1 1 1V20a1 1 0 0 1-1 1A17 17 0 0 1 3 4a1 1 0 0 1 1-1h3.5a1 1 0 0 1 1 1c0 1.25.2 2.45.57 3.6a1 1 0 0 1-.25 1z"/></svg>
        <span>587-412-6630</span>
      </li>
      <li>
        <svg viewBox="0 0 24 24" aria-hidden="true"><circle cx="12" cy="12" r="10" fill="none" stroke="var(--brand-pink)" stroke-width="2"/><path d="M2 12h20M12 2c3 3 3 17 0 20M12 2c-3 3-3 17 0 20M4 7h16M4 17h16" fill="none" stroke="var(--brand-pink)" stroke-width="1.6"/></svg>
        <span>info@meloraskin.com</span>
      </li>
    </ul>
  </section>

</body>
</html>
```